Harbor Spine Clinic needs Poster Design

We need a clean infographic which illustrates the ''3 phases of healing or pathway to health'' that a patient goes through when being under chiropractic care.

The design should match the logo design as well as the current posters that are in the office. Minimalistic yet noble and artsy. Attached will be the pictures that are currently up in the office. It would be great if the infographic would have the same ''background colours'' as the current pictures in the office or at least be somewhat similar in style.

If someone can recreate this in the style of a DelPorto drawing that would be my dream!

I do want the design to be as clean and minimalistic as possible while at the same time conveying the maximum amount of information. What I would like to be part of the design is the following:
- 1) The 3 phases: Acute phase, Repair phase, Maintenance phase
- 2) An indication of a timeline going from right to left and a trajectory going upwards from bottom to the top
- 3) An indicator that shows that transitioning into the phases there is the possibility of relapsing and losing progress as well as it being a point to make a decision.
- 4) Explanations are not a necessity as far as long texts are concerned if the design is clean and easy to understand.

Also, attached some ideas of how this poster has been created by others with the ''3 stages of healing or pathway to health''.

Target Market(s)

Patients who need to understand how proper healing occurs. That problems who have been around for many years, take time to heal. Also, that healing is not a linear process but there will be ups and downs

Industry/Entity Type

Optimal Health

Requirements
Nice to have
• Del Porto style!!!

```html
<!DOCTYPE html>
<html lang="en">
<head>
<meta charset="utf-8">
<title>Pathway to Health</title>
<link rel="stylesheet" href="https://fonts.googleapis.com/css2?family=IM+Fell+English&family=Cedarville+Cursive&family=Dancing+Script:wght@400&display=swap">
<style>
  :root {
    --paper-light: #f2e9d6;
    --paper-mid: #e8dabd;
    --paper-edge: #cdb68f;
    --ink: #4a2a1c;
    --ink-soft: rgba(74, 42, 28, 0.55);
    --line-faint: rgba(90, 70, 55, 0.45);
    --sketch-warm: rgba(150, 80, 55, 0.38);
    --sketch-fade: rgba(190, 130, 100, 0);
    --curve-red: #a3121b;
  }
  * { margin: 0; padding: 0; box-sizing: border-box; }
  html, body { width: 1200px; height: 848px; overflow: hidden; background: var(--paper-mid); }
  .poster {
    position: relative;
    width: 1200px;
    height: 848px;
    overflow: hidden;
    color: var(--ink);
    background:
      radial-gradient(ellipse at 55% 40%, var(--paper-light) 0%, var(--paper-mid) 65%, var(--paper-edge) 100%);
  }
  .chart { position: absolute; inset: 0; }
  .poster-title {
    position: absolute;
    left: 86px;
    top: 44px;
    font-family: "IM Fell English", serif;
    font-weight: 400;
    font-size: 36px;
    line-height: 44px;
    letter-spacing: 5px;
    color: var(--ink);
    white-space: nowrap;
  }
  .axis-label {
    position: absolute;
    font-family: "Cedarville Cursive", cursive;
    font-size: 22px;
    line-height: 28px;
    color: var(--ink);
    white-space: nowrap;
  }
  .axis-label--healing { left: 102px; top: 228px; transform: rotate(-90deg); transform-origin: left top; }
  .axis-label--time { left: 1027px; top: 780px; }
  .phase { position: absolute; }
  .phase-title {
    font-family: "Dancing Script", cursive;
    font-weight: 400;
    font-size: 27px;
    line-height: 34px;
    color: var(--ink);
    white-space: nowrap;
  }
  .phase-text {
    font-family: "Cedarville Cursive", cursive;
    font-size: 10.5px;
    line-height: 19.5px;
    color: var(--ink);
  }
  .phase--acute .phase-title { position: absolute; left: 81px; top: 414px; }
  .phase--acute .phase-text { position: absolute; left: 81px; top: 462px; width: 232px; }
  .phase--repair .phase-title { position: absolute; left: 292px; top: 152px; }
  .phase--repair .phase-text { position: absolute; left: 298px; top: 206px; width: 232px; }
  .phase--maintenance .phase-title { position: absolute; left: 660px; top: 66px; font-size: 29px; }
  .phase--maintenance .phase-text { position: absolute; left: 938px; top: 79px; width: 218px; }
  .phase--relapse .phase-title { position: absolute; left: 720px; top: 436px; }
  .phase--relapse .phase-text { position: absolute; left: 877px; top: 446px; width: 228px; }
</style>
</head>
<body>
<main class="poster">
  <svg class="chart" width="1200" height="848" viewBox="0 0 1200 848" xmlns="http://www.w3.org/2000/svg">
    <defs>
      <radialGradient id="sketchTone" cx="50%" cy="50%" r="50%">
        <stop offset="0%" stop-color="var(--sketch-warm)"/>
        <stop offset="100%" stop-color="var(--sketch-fade)"/>
      </radialGradient>
    </defs>

    <g class="sketch-area" role="img" aria-label="Sepia anatomical sketch of muscle fibres twisting upward along the healing curve, with a branching tangle marking relapse risk">
      <ellipse cx="520" cy="440" rx="430" ry="120" transform="rotate(-38 520 440)" fill="url(#sketchTone)"/>
      <ellipse cx="220" cy="695" rx="95" ry="75" fill="url(#sketchTone)"/>
      <ellipse cx="700" cy="530" rx="110" ry="70" transform="rotate(25 700 530)" fill="url(#sketchTone)"/>
    </g>

    <g class="axes" stroke="var(--line-faint)" stroke-width="1.2" fill="none">
      <line x1="139" y1="142" x2="139" y2="780"/>
      <line x1="139" y1="776" x2="1095" y2="776"/>
      <polyline points="1085,772 1095,776 1088,783"/>
    </g>

    <g class="phase-markers" stroke="var(--ink-soft)" stroke-width="1" fill="none">
      <circle cx="225" cy="698" r="82"/>
      <circle cx="548" cy="405" r="68"/>
      <circle cx="795" cy="214" r="101"/>
      <circle cx="653" cy="480" r="31"/>
      <line x1="150" y1="604" x2="172" y2="630"/>
      <line x1="450" y1="334" x2="502" y2="352"/>
      <line x1="765" y1="101" x2="771" y2="118"/>
    </g>

    <path class="healing-curve" fill="none" stroke="var(--curve-red)" stroke-width="2.4" stroke-linecap="round"
      d="M228,667 C250,650 280,680 260,697 C240,712 175,700 175,680 C178,650 250,640 290,700 C310,730 340,740 380,720 C440,690 470,620 520,540 C570,460 630,330 710,240 C760,190 820,165 920,148"/>
  </svg>

  <h1 class="poster-title">PATHWAY to HEALTH</h1>
  <span class="axis-label axis-label--healing">Healing</span>
  <span class="axis-label axis-label--time">Time</span>

  <section class="phase phase--acute">
    <h2 class="phase-title">1. Acute Phase</h2>
    <p class="phase-text">The Acute phase is the initial stage of healing and can last anywhere from a few days to a few weeks. During this time, the body is in a state of heightened inflammation, as the immune system is working to fight off infection and begin the healing process. This phase is characterized by redness, swelling, heat, and pain.</p>
  </section>

  <section class="phase phase--repair">
    <h2 class="phase-title">2. Repair phase</h2>
    <p class="phase-text">The Repair phase is the second stage of healing and usually lasts for several weeks. During this time, the body is actively rebuilding and repairing damaged tissues. This phase is characterized by the formation of new blood vessels, the development of new collagen and elastin fibers, and the formation of scar tissue.</p>
  </section>

  <section class="phase phase--maintenance">
    <h2 class="phase-title">3. Maintenance phase</h2>
    <p class="phase-text">Maintenance Phase: The Maintenance phase is the final stage of healing and can last for several months or even years. During this time, the body is actively remodeling and strengthening the repaired tissues. This phase is characterized by the formation of new collagen fibers, increased muscle strength, and improved mobility.</p>
  </section>

  <section class="phase phase--relapse">
    <h2 class="phase-title">Relapse risk</h2>
    <p class="phase-text">Relapse risk on the path to healing with a chronic illness is real if the care is not continued. After a period of symptom management, remission, and a return to normal activities, recurrence of the illness can be triggered by any number of factors. Stress, lack of sleep, and poor nutrition can all contribute to a weakening of the body's defenses and lead to a relapse.</p>
  </section>
</main>
</body>
</html>
```